App für weniger Konsum
Zielgruppe
Wir sind ein Startup, das Nutzer:innen in einem bewussteren Kaufverhalten stärkt. Dabei werden Nutzer:innen psychologischen Kaufprofilen zugeordnet und individuell auf dem Weg begleitet, weniger einzukaufen. Das stärkt die Finanzen und schützt die Umwelt.
Aufgabenstellung
Das Design sollte einerseits minimalismusorientierte Nutzer:innen ansprechen (clean, ruhig), aber auch Nutzer:innen ansprechen, die sich noch nicht mit weniger / besserem Konsum beschäftigt haben.
Es wäre toll folgende Slides zu haben:
- Anmeldung / Registrierung
- Quiz (Es soll direkt zu Beginn ein Quiz aus mehreren Slides geben, das Nutzer:innen einem Kauftypen zuordnet(
- Quizergebnis (Du bist Kauftyp XYZ...)
- Home-Screen der App / Navigation
- Statistiken: Du hast diesen Monat so viel gespart...
- Slide mit Einstellungen
- 'Challenge' Slide: 10 tage aussortieren

```html
<!DOCTYPE html>
<html lang="de">
<head>
<meta charset="utf-8">
<title>minda – App-Screens</title>
<link rel="stylesheet" href="https://fonts.googleapis.com/css2?family=Barlow:wght@400;500;600;700&display=swap">
<style>
:root{
  --page:#050607;
  --screen:#19343a;
  --screen-deep:#162d32;
  --card:#21434a;
  --card-soft:#25484f;
  --status:#2b2e30;
  --pink:#f8c3da;
  --pink-strong:#f0609b;
  --mint:#2ff0b4;
  --mint-soft:#b9f5e2;
  --text:#e9f1f1;
  --muted:#b7c8c9;
  --line:#6fa5ad;
}
*{box-sizing:border-box;margin:0;padding:0}
html,body{width:1200px;height:438px;overflow:hidden;background:var(--page)}
body{font-family:"Barlow",sans-serif;color:var(--text);position:relative}
.phone{position:absolute;top:23px;width:176px;height:392px;border-radius:22px;background:var(--screen);overflow:hidden}
.status{height:22px;background:var(--status);display:flex;align-items:center;justify-content:space-between;padding:0 9px 0 7px;font-size:6.5px;color:var(--text)}
.status svg{width:22px;height:6px}
.abs{position:absolute}
.logo{font-weight:600;color:var(--pink);letter-spacing:.5px;line-height:1}
.field{position:absolute;left:13px;width:150px;height:22px;border-radius:11px;border:1px solid var(--line);background:#24505a;font-size:7px;padding-left:17px;line-height:20px}
.btn{position:absolute;left:13px;width:150px;height:23px;border-radius:12px;font-size:7px;text-align:center;line-height:21px}
.btn-primary{background:var(--pink);color:#1a2f33;font-weight:600;line-height:23px}
.btn-outline{border:1px solid var(--text)}
.card{position:absolute;background:var(--card);border-radius:12px}
.art{position:absolute;border-radius:10px}
.label-sm{font-size:7px;font-weight:600}
.eyebrow{font-size:7.5px}
.headline{font-size:11px;font-weight:700;line-height:1.4}
.nav{position:absolute;left:0;right:0;bottom:0;height:54px;background:var(--screen);display:flex;justify-content:space-around;align-items:flex-start;padding-top:11px}
.nav-item{display:flex;flex-direction:column;align-items:center;gap:3px;font-size:7.5px;width:50px}
.nav-item svg{width:16px;height:16px}
.nav-item.active{color:var(--pink)}
.option{position:absolute;left:7px;width:118px;border-radius:8px;border:1px solid var(--text);font-size:7px;line-height:1.7;padding:4px 10px}
.bar-track{position:absolute;height:3px;border-radius:2px;background:#2f5a61}
.bar-fill{height:100%;border-radius:2px;background:var(--pink)}
.day{position:absolute;width:27px;height:54px;border-radius:14px;background:#224349;text-align:center;font-size:8px;font-weight:600}
.day .num{display:block;margin-top:6px}
.day .pill{position:absolute;left:3px;bottom:4px;width:21px;height:32px;border-radius:11px;border:1px solid #3f6b72;background:#1b3a3f;font-size:8px;font-weight:500;display:flex;flex-direction:column;align-items:center;justify-content:flex-end;padding-bottom:3px}
.day .pill.done{background:var(--mint);border-color:var(--mint);color:#1a3338}
.day .pill.miss{background:var(--pink-strong);border-color:var(--pink-strong);color:#1a3338}
.back{position:absolute;left:77px;top:361px;width:23px;height:23px;border-radius:50%;border:1.3px solid var(--text)}
.back svg{width:21px;height:21px}
</style>
</head>
<body>

<!-- Screen 1: Anmeldung -->
<section class="phone" style="left:19px">
  <div class="status"><span>10:00</span><svg viewBox="0 0 22 6"><path d="M0 6L5 1V6Z M8 1H14L11 6Z M17 1H19V6H17Z" fill="#e9f1f1"/></svg></div>
  <div class="abs logo" style="top:44px;left:0;right:0;text-align:center;font-size:20px">minda</div>
  <div class="abs" style="top:74px;left:0;right:0;text-align:center;font-size:11px;line-height:1.2">Anmelden</div>
  <div class="field" style="top:107px">E-Mail Adresse</div>
  <div class="field" style="top:138px">Passwort</div>
  <div class="btn btn-primary" style="top:169px">Anmelden</div>
  <div class="abs" style="top:198px;left:0;right:0;text-align:center;font-size:7px">Konto erstellen</div>
  <div class="abs" style="top:242px;left:18px;right:18px;height:1px;background:#4e7077"></div>
  <div class="abs" style="top:237px;left:73px;width:30px;text-align:center;font-size:7px;background:var(--screen)">oder</div>
  <div class="btn btn-outline" style="top:255px">Mit Glimmo anmelden</div>
  <div class="btn btn-outline" style="top:285px">Mit Frendoo anmelden</div>
  <div class="btn btn-outline" style="top:316px">Mit Aprika anmelden</div>
</section>

<!-- Screen 2: Home -->
<section class="phone" style="left:215px">
  <div class="status"><span>10:00</span><svg viewBox="0 0 22 6"><path d="M0 6L5 1V6Z M8 1H14L11 6Z M17 1H19V6H17Z" fill="#e9f1f1"/></svg></div>
  <div class="abs logo" style="top:37px;left:12px;font-size:15px">minda</div>
  <svg class="abs" style="top:36px;left:107px" width="14" height="14" viewBox="0 0 14 14" fill="none" stroke="#e9f1f1" stroke-width="1.2"><path d="M3 10V6a4 4 0 0 1 8 0v4l1 1H2Z M5.5 12.5h3"/></svg>
  <svg class="abs" style="top:36px;left:131px" width="4" height="14" viewBox="0 0 4 14" fill="#e9f1f1"><circle cx="2" cy="2" r="1.2"/><circle cx="2" cy="7" r="1.2"/><circle cx="2" cy="12" r="1.2"/></svg>
  <div class="abs" role="img" aria-label="Profilfoto" style="top:33px;left:145px;width:21px;height:21px;border-radius:50%;background:linear-gradient(#a07a5a,#3e3328)"></div>

  <div class="card" style="top:71px;left:9px;width:157px;height:87px">
    <div class="abs label-sm" style="top:8px;left:7px">Fortschritt <svg width="8" height="8" viewBox="0 0 8 8" style="vertical-align:-1px"><circle cx="4" cy="4" r="4" fill="#2ff0b4"/><path d="M2.5 5.5L5.5 2.5M3.5 2.5H5.5V4.5" stroke="#1a3338" stroke-width=".9" fill="none"/></svg></div>
    <div class="abs" style="top:23px;left:7px;font-size:7px;line-height:1">12.<br>02.</div>
    <svg class="abs" style="top:24px;left:23px" width="18" height="18" viewBox="0 0 18 18"><circle cx="9" cy="9" r="7" fill="none" stroke="#f8c3da" stroke-width="2.4" stroke-dasharray="33 44" transform="rotate(-90 9 9)"/></svg>
    <div class="abs" style="top:22px;left:45px;font-size:15px;font-weight:500">75<span style="font-size:8px">/100</span></div>
    <div class="abs" style="top:49px;left:7px;font-size:7px;line-height:1">13.<br>02.</div>
    <svg class="abs" style="top:50px;left:23px" width="18" height="18" viewBox="0 0 18 18"><circle cx="9" cy="9" r="7" fill="none" stroke="#f8c3da" stroke-width="2.4" stroke-dasharray="38 44" transform="rotate(-90 9 9)"/></svg>
    <div class="abs" style="top:48px;left:44px;font-size:15px;font-weight:500">86<span style="font-size:8px">/100</span></div>
    <div class="art" role="img" aria-label="Illustration: Wanderin mit Fernglas am Gipfel mit Fahne" style="top:14px;left:84px;width:62px;height:62px;background:linear-gradient(160deg,#2d5a5f,#1d3b40)"></div>
    <svg class="abs" style="top:69px;left:143px" width="7" height="10" viewBox="0 0 7 10"><path d="M1 1L6 5L1 9" stroke="#e9f1f1" stroke-width="1.2" fill="none"/></svg>
  </div>

  <div class="card" style="top:166px;left:9px;width:157px;height:87px">
    <div class="art" role="img" aria-label="Illustration: Person beim Gewichtheben" style="top:14px;left:8px;width:64px;height:56px;background:linear-gradient(160deg,#2d5a5f,#1d3b40)"></div>
    <div class="abs label-sm" style="top:10px;right:7px">Challenges</div>
    <div class="abs" style="top:28px;right:7px;font-size:7px">10-Tage-Challenge</div>
    <div class="bar-track" style="top:45px;left:79px;width:45px"><div class="bar-fill" style="width:100%"></div></div>
    <div class="abs" style="top:40px;right:7px;font-size:6.5px;font-weight:600">75%</div>
    <div class="abs" style="top:53px;right:7px;font-size:7px">Spar-Challenge</div>
    <div class="bar-track" style="top:71px;left:79px;width:45px"><div class="bar-fill" style="width:70%"></div></div>
    <div class="abs" style="top:66px;right:7px;font-size:6.5px;font-weight:600">55%</div>
    <svg class="abs" style="top:70px;left:11px" width="7" height="10" viewBox="0 0 7 10"><path d="M1 1L6 5L1 9" stroke="#e9f1f1" stroke-width="1.2" fill="none"/></svg>
  </div>

  <div class="card" style="top:262px;left:9px;width:157px;height:90px">
    <div class="abs label-sm" style="top:10px;left:10px">Statistik</div>
    <div class="abs" style="top:22px;left:65px;font-size:5px">12.02.</div>
    <svg class="abs" style="top:30px;left:8px" width="72" height="44" viewBox="0 0 72 44"><path d="M0 4H70" stroke="#6fa5ad" stroke-width=".5" stroke-dasharray="1 2"/><path d="M66 0V44" stroke="#6fa5ad" stroke-width=".5"/><g stroke-linecap="round" stroke-width="3.5" stroke="#b9f5e2"><path d="M4 42V38M17 42V12M33 42V26M48 42V38M63 42V28"/></g><path d="M70 42V38" stroke="#f8c3da" stroke-width="3.5" stroke-linecap="round"/><text x="22" y="11" font-size="5" fill="#e9f1f1">54€</text></svg>
    <div class="art" role="img" aria-label="Illustration: Person präsentiert Diagramme an einer Tafel" style="top:18px;left:88px;width:62px;height:60px;background:linear-gradient(160deg,#2d5a5f,#1d3b40)"></div>
  </div>

  <nav class="nav">
    <div class="nav-item active"><svg viewBox="0 0 16 16" fill="none" stroke="#f8c3da" stroke-width="1.2"><path d="M2 7L8 2L14 7V14H10V10H6V14H2Z"/></svg>Home</div>
    <div class="nav-item"><svg viewBox="0 0 16 16" fill="none" stroke="#e9f1f1" stroke-width="1.2"><path d="M3 14V12M6.5 14V9M10 14V5M13.5 14V1"/></svg>Statistik</div>
    <div class="nav-item"><svg viewBox="0 0 16 16" fill="none" stroke="#e9f1f1" stroke-width="1.2"><path d="M4 2H12V6A4 4 0 0 1 4 6Z M4 3H1.5A2.5 2.5 0 0 0 4 7 M12 3H14.5A2.5 2.5 0 0 1 12 7 M8 10V13 M5 14H11"/></svg>Challenges</div>
  </nav>
</section>

<!-- Screen 3: Quiz -->
<section class="phone" style="left:411px">
  <div class="status"><span>10:00</span><svg viewBox="0 0 22 6"><path d="M0 6L5 1V6Z M8 1H14L11 6Z M17 1H19V6H17Z" fill="#e9f1f1"/></svg></div>
  <div class="abs eyebrow" style="top:46px;left:22px">Mini Quiz</div>
  <div class="abs headline" style="top:61px;left:22px">Welcher Kauftyp<br>bist du?</div>
  <div class="card" style="top:109px;left:20px;width:129px;height:223px;background:var(--card-soft)">
    <div class="abs" style="top:10px;left:12px;font-size:11px;font-weight:700">Frage 1</div>
    <svg class="abs" style="top:10px;right:11px" width="14" height="14" viewBox="0 0 14 14" fill="none" stroke="#e9f1f1" stroke-width="1"><path d="M7 13A6 6 0 1 0 2 10L1.5 13L4 12A6 6 0 0 0 7 13Z"/><path d="M5.3 5.3A1.7 1.7 0 1 1 7 7V8.2"/><circle cx="7" cy="10" r=".4" fill="#e9f1f1"/></svg>
    <div class="abs" style="top:34px;left:12px;font-size:7.5px;line-height:1.6">Wenn du etwas siehst,<br>das du magst …</div>
    <div class="option" style="top:81px;background:var(--pink);border-color:var(--pink);color:#1a2f33;font-weight:600;height:26px;line-height:18px">… kaufst du es meist direkt.</div>
    <div class="option" style="top:117px;height:50px">… legst du es in den Warenkorb und überlegst später.</div>
    <div class="option" style="top:177px;height:38px">… notierst du es und wartest bewusst ab.</div>
  </div>
  <div class="card" style="top:109px;left:161px;width:40px;height:223px;background:var(--card-soft)">
    <div class="abs" style="top:10px;left:10px;font-size:11px;font-weight:700">F</div>
    <div class="abs" style="top:81px;left:7px;width:40px;height:26px;border-radius:8px;background:var(--pink)"></div>
    <div class="abs" style="top:117px;left:7px;width:40px;height:50px;border-radius:8px;border:1px solid var(--text)"></div>
    <div class="abs" style="top:177px;left:7px;width:40px;height:38px;border-radius:8px;border:1px solid var(--text)"></div>
  </div>
  <svg class="abs" style="top:350px;left:73px" width="32" height="6" viewBox="0 0 32 6"><circle cx="3" cy="3" r="2.4" fill="#e9f1f1"/><circle cx="16" cy="3" r="2.4" fill="#557d84"/><circle cx="29" cy="3" r="2.4" fill="#557d84"/></svg>
</section>

<!-- Screen 4: Quizergebnis -->
<section class="phone" style="left:608px">
  <div class="status"><span>10:00</span><svg viewBox="0 0 22 6"><path d="M0 6L5 1V6Z M8 1H14L11 6Z M17 1H19V6H17Z" fill="#e9f1f1"/></svg></div>
  <div class="abs eyebrow" style="top:46px;left:22px">Mini Quiz</div>
  <div class="abs headline" style="top:60px;left:22px">Dein Ergebnis</div>
  <div class="art" role="img" aria-label="Illustration: Person mit Schmetterlingsnetz jagt einen Rabatt-Schmetterling" style="top:94px;left:14px;width:150px;height:172px;background:radial-gradient(circle at 50% 50%,#2b5a60,#19343a 75%)"></div>
  <div class="abs" style="top:273px;left:0;right:0;text-align:center;font-size:11px;font-weight:700">Sticker-Chaser</div>
  <div class="abs" style="top:297px;left:12px;right:12px;text-align:center;font-size:7px;line-height:1.7">Siehst Du bei Rabatten plötzlich rot?<br>kein Ding! minda gibt deinen Käufen<br>grünes Licht.</div>
  <div class="back"><svg viewBox="0 0 21 21"><path d="M12 6L8 10.5L12 15" stroke="#e9f1f1" stroke-width="1.3" fill="none"/></svg></div>
</section>

<!-- Screen 5: Statistik -->
<section class="phone" style="left:804px">
  <div class="status"><span>10:00</span><svg viewBox="0 0 22 6"><path d="M0 6L5 1V6Z M8 1H14L11 6Z M17 1H19V6H17Z" fill="#e9f1f1"/></svg></div>
  <div class="abs" style="top:22px;left:0;right:0;height:132px;background:var(--screen-deep)"></div>
  <div class="abs label-sm" style="top:32px;left:12px;font-size:7.5px">Wochenübersicht</div>
  <svg class="abs" style="top:44px;left:0" width="176" height="110" viewBox="0 0 176 110">
    <text x="60" y="6" font-size="5" fill="#e9f1f1">05.02.</text>
    <text x="152" y="6" font-size="5" fill="#e9f1f1">12.02.</text>
    <path d="M0 26H176" stroke="#6fa5ad" stroke-width=".5" stroke-dasharray="1 2"/>
    <path d="M67 10V95M161 10V95" stroke="#6fa5ad" stroke-width=".5"/>
    <text x="75" y="29" font-size="5" fill="#e9f1f1">54€</text>
    <g stroke="#b9f5e2" stroke-width="4" stroke-linecap="round">
      <path d="M2 92V56M15 92V76M28 92V88M41 92V70M54 92V88M80 92V88M93 92V88M106 92V56M119 92V76M132 92V88M145 92V72"/>
    </g>
    <g stroke="#f8c3da" stroke-width="4" stroke-linecap="round"><path d="M67 92V28M158 92V88"/></g>
    <g font-size="5.5" fill="#e9f1f1" text-anchor="middle">
      <text x="2" y="103">Mi</text><text x="15" y="103">Do</text><text x="28" y="103">Fr</text><text x="41" y="103">Sa</text><text x="54" y="103">So</text><text x="67" y="103">Mo</text><text x="80" y="103">Di</text><text x="93" y="103">Mi</text><text x="106" y="103">Do</text><text x="119" y="103">Fr</text><text x="132" y="103">Sa</text><text x="145" y="103">So</text><text x="158" y="103">Mo</text>
    </g>
    <path d="M89 108H165" stroke="#557d84" stroke-width="1"/>
  </svg>

  <div class="card" style="top:166px;left:10px;width:104px;height:81px">
    <div class="abs label-sm" style="top:8px;left:11px">Fortschritt</div>
    <svg class="abs" style="top:6px;right:8px" width="14" height="14" viewBox="0 0 14 14"><circle cx="7" cy="7" r="7" fill="#2ff0b4"/><path d="M4.5 9.5L9.5 4.5M5.5 4.5H9.5V8.5" stroke="#1a3338" stroke-width="1.2" fill="none"/></svg>
    <svg class="abs" style="top:21px;left:7px" width="44" height="44" viewBox="0 0 44 44"><circle cx="22" cy="22" r="19.5" fill="none" stroke="#2f5a61" stroke-width="2.6"/><circle cx="22" cy="22" r="19.5" fill="none" stroke="#f8c3da" stroke-width="2.6" stroke-dasharray="92 123" transform="rotate(-90 22 22)"/></svg>
    <div class="abs" style="top:35px;left:13px;font-size:14px;font-weight:500">75%</div>
    <div class="abs" style="top:68px;left:18px;font-size:6.5px">Gesamt</div>
    <div class="abs" style="top:28px;left:62px;font-size:6.5px">Käufe</div>
    <svg class="abs" style="top:42px;left:63px" width="26" height="16" viewBox="0 0 26 16"><g fill="#2ff0b4"><circle cx="3" cy="3" r="2.6"/><circle cx="12" cy="3" r="2.6"/><circle cx="21" cy="3" r="2.6"/></g><g fill="#f0609b"><circle cx="3" cy="12" r="2.6"/><circle cx="12" cy="12" r="2.6"/></g></svg>
    <div class="abs" style="top:58px;left:62px;font-size:11px;font-weight:500">3<span style="font-size:7px">/5</span></div>
    <svg class="abs" style="top:61px;left:89px" width="7" height="10" viewBox="0 0 7 10"><path d="M1 1L6 5L1 9" stroke="#e9f1f1" stroke-width="1.2" fill="none"/></svg>
  </div>
  <div class="card" style="top:166px;left:123px;width:45px;height:81px;text-align:center">
    <svg class="abs" style="top:6px;left:15px" width="15" height="15" viewBox="0 0 15 15" fill="none" stroke="#e9f1f1" stroke-width="1"><path d="M4 11V7a4 4 0 0 1 7 0v4l1 1H3Z M6 13.5h3 M1.5 5A6 6 0 0 1 4 2 M13.5 5A6 6 0 0 0 11 2"/></svg>
    <div class="abs" style="top:24px;left:0;right:0;font-size:11px;font-weight:500">16</div>
    <div class="abs" style="top:38px;left:0;right:0;font-size:6.5px">Alerts</div>
    <div class="abs" style="top:50px;left:0;right:0;font-size:11px;font-weight:500">13</div>
    <div class="abs" style="top:64px;left:0;right:0;font-size:6.5px">Reaktionen</div>
  </div>

  <div class="card" style="top:260px;left:10px;width:160px;height:90px">
    <div class="abs label-sm" style="top:11px;left:15px">Challenges</div>
    <div class="abs" style="top:11px;left:85px;font-size:7px;display:flex;gap:5px;align-items:center">
      <span><svg width="6" height="6"><circle cx="3" cy="3" r="3" fill="#2ff0b4"/></svg> 8</span>
      <span><svg width="6" height="6"><circle cx="3" cy="3" r="3" fill="#10262a"/></svg> 15</span>
      <span><svg width="6" height="6"><circle cx="3" cy="3" r="3" fill="#f0609b"/></svg> 3</span>
    </div>
    <div class="abs" style="top:31px;left:12px;font-size:6.5px">10-Tage-Challenge</div>
    <div class="bar-track" style="top:35px;left:82px;width:35px"><div class="bar-fill" style="width:100%"></div></div>
    <div class="abs" style="top:30px;left:121px;font-size:6.5px;font-weight:600">75%</div>
    <div class="abs" style="top:50px;left:12px;font-size:6.5px">Spar-Challenge</div>
    <div class="bar-track" style="top:54px;left:82px;width:35px"><div class="bar-fill" style="width:65%"></div></div>
    <div class="abs" style="top:49px;left:121px;font-size:6.5px;font-weight:600">55%</div>
    <div class="abs" style="top:69px;left:12px;font-size:6.5px">Wochen-Challenge</div>
    <div class="bar-track" style="top:73px;left:82px;width:35px"><div class="bar-fill" style="width:40%"></div></div>
    <div class="abs" style="top:68px;left:121px;font-size:6.5px;font-weight:600">35%</div>
    <svg class="abs" style="top:30px;left:144px" width="7" height="48" viewBox="0 0 7 48" fill="none" stroke="#e9f1f1" stroke-width="1.2"><path d="M1 1L6 5L1 9M1 20L6 24L1 28M1 39L6 43L1 47"/></svg>
    <div class="abs" style="top:28px;left:153px;width:1px;height:50px;background:#557d84"></div>
  </div>

  <nav class="nav">
    <div class="nav-item active"><svg viewBox="0 0 16 16" fill="none" stroke="#f8c3da" stroke-width="1.2"><path d="M2 7L8 2L14 7V14H10V10H6V14H2Z"/></svg>Home</div>
    <div class="nav-item"><svg viewBox="0 0 16 16" fill="none" stroke="#e9f1f1" stroke-width="1.2"><path d="M3 14V12M6.5 14V9M10 14V5M13.5 14V1"/></svg>Statistik</div>
    <div class="nav-item"><svg viewBox="0 0 16 16" fill="none" stroke="#e9f1f1" stroke-width="1.2"><path d="M4 2H12V6A4 4 0 0 1 4 6Z M4 3H1.5A2.5 2.5 0 0 0 4 7 M12 3H14.5A2.5 2.5 0 0 1 12 7 M8 10V13 M5 14H11"/></svg>Challenges</div>
  </nav>
</section>

<!-- Screen 6: Challenge -->
<section class="phone" style="left:1000px">
  <div class="status"><span>10:00</span><svg viewBox="0 0 22 6"><path d="M0 6L5 1V6Z M8 1H14L11 6Z M17 1H19V6H17Z" fill="#e9f1f1"/></svg></div>
  <div class="abs eyebrow" style="top:44px;left:13px">Challenge</div>
  <div class="abs headline" style="top:61px;left:13px">10 Tage aussortieren</div>
  <div class="abs" style="top:88px;left:13px;right:10px;font-size:7px;line-height:1.7">10 Tage lang helfen wir dir dabei, unwichtige Dinge auszusortieren. Unsere Push-Nach-richten werden dich anspornen!</div>

  <div class="day" style="top:139px;left:12px"><span class="num">1</span><div class="pill done"><svg width="12" height="10" viewBox="0 0 12 10"><path d="M1 5L4.5 8.5L11 1" stroke="#1a3338" stroke-width="1.3" fill="none"/></svg>3/3</div></div>
  <div class="day" style="top:139px;left:44px"><span class="num">2</span><div class="pill miss"><svg width="10" height="10" viewBox="0 0 10 10"><path d="M1 1L9 9M9 1L1 9" stroke="#1a3338" stroke-width="1.3"/></svg>1/3</div></div>
  <div class="day" style="top:139px;left:75px"><span class="num">3</span><div class="pill done"><svg width="12" height="10" viewBox="0 0 12 10"><path d="M1 5L4.5 8.5L11 1" stroke="#1a3338" stroke-width="1.3" fill="none"/></svg>3/3</div></div>
  <div class="day" style="top:139px;left:106px"><span class="num">4</span><div class="pill done"><svg width="12" height="10" viewBox="0 0 12 10"><path d="M1 5L4.5 8.5L11 1" stroke="#1a3338" stroke-width="1.3" fill="none"/></svg>3/3</div></div>
  <div class="day" style="top:139px;left:137px"><span class="num">5</span><div class="pill">0/3</div></div>

  <div class="day" style="top:204px;left:12px"><span class="num">10</span><div class="pill">0/3</div></div>
  <div class="day" style="top:204px;left:44px"><span class="num">10</span><div class="pill">0/3</div></div>
  <div class="day" style="top:204px;left:75px"><span class="num">10</span><div class="pill">0/3</div></div>
  <div class="day" style="top:204px;left:106px"><span class="num">10</span><div class="pill">0/3</div></div>
  <div class="day" style="top:204px;left:137px"><span class="num">10</span><div class="pill">0/3</div></div>

  <div class="bar-track" style="top:284px;left:11px;width:109px;height:4px"><div class="bar-fill" style="width:53%"></div></div>
  <div class="abs" style="top:277px;left:128px;font-size:11px;font-weight:500">45%</div>
  <svg class="abs" style="top:277px;left:155px" width="14" height="14" viewBox="0 0 14 14"><circle cx="7" cy="7" r="7" fill="#2ff0b4"/><path d="M4.5 9.5L9.5 4.5M5.5 4.5H9.5V8.5" stroke="#1a3338" stroke-width="1.2" fill="none"/></svg>
  <div class="abs" style="top:303px;left:13px;right:8px;font-size:7px;line-height:1.7">Nur noch 6 Tage. Du bist auf einem guten Weg, weiter so!</div>
  <div class="back"><svg viewBox="0 0 21 21"><path d="M12 6L8 10.5L12 15" stroke="#e9f1f1" stroke-width="1.3" fill="none"/></svg></div>
</section>

</body>
</html>
```